Martin Halvorsen Pianist Teacher Examiner

I need a website design to promote my business as a professional classical pianist and a piano teacher of all levels.
I want it to look a mixture of old world opulence (eg antique grand piano?) and modern text. It should have an elegant, beautiful and relaxing feel.

Industry/Entity Type

Teacher

```html
<!DOCTYPE html>
<html lang="en">
<head>
<meta charset="utf-8">
<title>Martin Halvorsen – Classical Pianist and Piano Teacher</title>
<link rel="stylesheet" href="https://fonts.googleapis.com/css2?family=Montserrat:wght@400;500&family=Quicksand:wght@300;400;500&family=Open+Sans:ital,wght@0,400;0,600;1,400&display=swap">
<style>
:root{
  --ink:#222;
  --header:#2a2a2a;
  --hero-dark:#262626;
  --hero-mid:#3a3a3a;
  --orange:#f39a3a;
  --orange-deep:#ea8a2a;
  --white:#fff;
  --text-grey:#6a6a6a;
  --light-bg:#f5f5f5;
  --footer:#2c2c2c;
  --muted:#9a9a9a;
}
*{box-sizing:border-box;margin:0;padding:0}
html,body{width:740px;height:1200px;overflow:hidden}
body{position:relative;background:var(--white);font-family:"Open Sans",Arial,sans-serif;color:var(--ink)}
.abs{position:absolute}

/* header */
.site-header{left:0;top:0;width:740px;height:74px;background:repeating-linear-gradient(135deg,#2e2e2e 0 2px,#262626 2px 4px)}
.nav{top:36px;display:flex;gap:20px;font-family:"Montserrat",sans-serif;font-size:11px;font-weight:500;color:var(--white);letter-spacing:.2px}
.nav a{color:inherit;text-decoration:none}
.nav .active{color:var(--orange)}
.nav-left{left:82px}
.nav-right{left:479px}
.brand{left:270px;width:196px;top:20px;text-align:center;font-family:"Quicksand",sans-serif;color:var(--white)}
.brand-name{font-size:21px;font-weight:500;line-height:1.1}
.brand-name span{color:var(--orange)}
.brand-slogan{font-family:"Open Sans",sans-serif;font-size:9px;color:#b5b5b5;margin-top:1px}

/* hero */
.hero{left:0;top:74px;width:740px;height:348px;background:radial-gradient(circle at 70% 40%,var(--hero-mid),var(--hero-dark) 75%)}
.hero-portrait{left:280px;top:74px;width:400px;height:348px;background:radial-gradient(ellipse at 50% 45%,#b48a75 0 22%,#5a4a44 40%,#1f1f1f 72%,rgba(30,30,30,0) 80%)}
.hero-title{left:64px;top:172px;font-family:"Quicksand",sans-serif;font-weight:400;color:var(--white);font-size:27px;line-height:1.15}
.hero-title strong{display:block;color:var(--orange);font-weight:400;font-size:38px;line-height:1.05}
.hero-text{left:65px;top:244px;width:245px;font-size:8.3px;line-height:13.5px;color:#c9c9c9}
.hero-dots{left:65px;top:291px;display:flex;gap:3px}
.hero-dots i{width:7px;height:7px;border-radius:50%;background:#777}
.hero-dots i:first-child{background:var(--white)}
.hero-arrow{top:198px;width:30px;height:48px;background:#1b1b1b}
.hero-arrow.prev{left:0}
.hero-arrow.next{left:710px}

/* features */
.feature{top:445px;width:198px}
.feature-photo{width:198px;height:96px}
.feature-band{display:block;width:198px;height:12px}
.feature h3{margin-top:11px;font-family:"Montserrat",sans-serif;font-weight:400;font-size:14px;color:var(--ink)}
.feature p{margin-top:4px;font-size:8.3px;line-height:12px;color:var(--text-grey);padding-left:2px}
.btn{margin-top:11px;margin-left:2px;display:inline-block}
.f1{left:60px}.f2{left:271px}.f3{left:482px}

/* about */
.about{left:0;top:670px;width:740px;height:240px;background:var(--light-bg)}
.about-title{left:61px;top:716px;font-family:"Quicksand",sans-serif;font-weight:400;font-size:20px;color:#555}
.about-text{left:62px;width:328px;font-size:8.3px;line-height:12px;color:var(--text-grey)}
.about-text.one{top:747px}
.about-text.two{top:792px}
.video{left:425px;top:706px;width:228px;height:148px;background:var(--white);border:1px solid #e2e2e2;box-shadow:0 1px 3px rgba(0,0,0,.08)}
.video-still{left:4px;top:4px;width:220px;height:140px;background:linear-gradient(100deg,#8a8a8a,#2a2a2a 35%,#3a3a3a 60%,#1e1e1e)}
.video-play{left:95px;top:55px}

/* testimonials */
.testimonials{left:0;top:900px;width:740px;height:222px}
.testimonials-bg{left:0;top:0}
.testimonials-title{left:0;top:45px;width:740px;text-align:center;font-family:"Quicksand",sans-serif;font-weight:400;font-size:21px;color:var(--white)}
.quote{width:170px}
.quote-avatar{left:0;top:0;width:50px;height:50px;border-radius:50%;border:2px solid var(--white);background:radial-gradient(circle at 50% 45%,#c9a08a,#5a3d30)}
.quote p{margin-left:55px;font-style:italic;font-size:7.8px;line-height:13px;color:var(--white)}
.quote cite{display:block;margin-left:55px;margin-top:3px;font-style:normal;font-size:8.5px;color:var(--white)}
.q1{left:62px;top:88px}
.q2{left:274px;top:91px}
.q3{left:487px;top:91px}

/* footer */
.site-footer{left:0;top:1122px;width:740px;height:78px;background:var(--footer)}
.footer-nav{left:59px;top:25px;font-family:"Montserrat",sans-serif;font-size:10.5px;color:var(--white)}
.footer-nav span{margin:0 5px}
.copyright{left:59px;top:43px;font-size:7.5px;color:var(--muted)}
.social{left:608px;top:22px;display:flex;gap:9px}
.social i{width:17px;height:17px;border-radius:50%;background:var(--white)}
</style>
</head>
<body>

<header class="site-header abs" role="banner"></header>
<nav class="nav nav-left abs"><a class="active">HOME</a><a>ABOUT ME</a><a>SERVICES</a></nav>
<div class="brand abs">
  <div class="brand-name">Martin <span>Halvorsen</span></div>
  <div class="brand-slogan">slogan goes here</div>
</div>
<nav class="nav nav-right abs"><a>BLOG</a><a>TESTIMONIAL</a><a>CONTACT</a></nav>

<section class="hero abs"></section>
<div class="hero-portrait abs" role="img" aria-label="Portrait of the pianist in glasses and a leather jacket, chin resting on hand"></div>
<h1 class="hero-title abs">Classical Pianist and<strong>Piano teacher</strong></h1>
<p class="hero-text abs">Aliquam nec erat at purus cursus interdum Vestibulum ligula augue bibendum accumsan vestibulum ut commodo a mi Morbi ornare gravida elit Integer congue augue</p>
<div class="hero-dots abs"><i></i><i></i><i></i><i></i></div>
<div class="hero-arrow prev abs"><svg width="30" height="48"><polyline points="19,12 8,24 19,36" fill="none" stroke="#bbb" stroke-width="1.2"/></svg></div>
<div class="hero-arrow next abs"><svg width="30" height="48"><polyline points="11,12 22,24 11,36" fill="none" stroke="#bbb" stroke-width="1.2"/></svg></div>

<article class="feature f1 abs">
  <div class="feature-photo" role="img" aria-label="Man in leather jacket beside a white piano" style="background:linear-gradient(90deg,#e9e9e9 0 35%,#2a2a2a 55%,#1c1c1c)"></div>
  <svg class="feature-band" viewBox="0 0 198 12"><polygon points="0,0 198,0 198,4 0,12" fill="var(--orange)"/></svg>
  <h3>WHY CHOOSE ME?</h3>
  <p>Aliquam nec erat at purus cursus interdum Vestibu-lum ligula augue bibendum accumsan ves</p>
  <svg class="btn" width="74" height="21"><polygon points="0,0 66,0 74,10.5 66,21 0,21" fill="#333"/><text x="12" y="14" font-family="Montserrat,sans-serif" font-size="7.5" font-weight="500" fill="#fff">READ MORE</text></svg>
</article>

<article class="feature f2 abs">
  <div class="feature-photo" role="img" aria-label="Young woman playing the violin" style="background:radial-gradient(ellipse at 45% 50%,#a0683a,#2a1a10 55%,#0d0d0d)"></div>
  <svg class="feature-band" viewBox="0 0 198 12"><polygon points="0,0 198,0 198,4 0,4" fill="var(--orange)"/></svg>
  <h3>ALL LEVEL TEACHING</h3>
  <p>Aliquam nec erat at purus cursus interdum Vestibu-lum ligula augue bibendum ac</p>
  <svg class="btn" width="74" height="21"><polygon points="0,0 66,0 74,10.5 66,21 0,21" fill="#333"/><text x="12" y="14" font-family="Montserrat,sans-serif" font-size="7.5" font-weight="500" fill="#fff">READ MORE</text></svg>
</article>

<article class="feature f3 abs">
  <div class="feature-photo" role="img" aria-label="Hands playing piano keys" style="background:linear-gradient(180deg,#1a1a1a 0 12%,#e8e8e8 14% 55%,#d7a88c 70%,#111)"></div>
  <svg class="feature-band" viewBox="0 0 198 12"><polygon points="0,0 198,0 198,12 0,4" fill="var(--orange)"/></svg>
  <h3>MAKE AN APPOINTMENT</h3>
  <p>Aliquam nec erat at purus cursus interdum Vestibu-lum ligula augue bibendum accumsan vestib</p>
  <svg class="btn" width="74" height="21"><polygon points="0,0 66,0 74,10.5 66,21 0,21" fill="#333"/><text x="13" y="14" font-family="Montserrat,sans-serif" font-size="7.5" font-weight="500" fill="#fff">CLICK HERE</text></svg>
</article>

<section class="about abs"></section>
<h2 class="about-title abs">Little About Me</h2>
<p class="about-text one abs">Etiam eu urna Sed porta Suspendisse quam leo molestie sed luctus quis feugiat in pede Fusce tellus Sed metus augue convallis et vehicula ut pulvinar eu ante Integer orci tellus tristique vitae consequat nec porta vel lectus Nulla sit amet diam</p>
<p class="about-text two abs">Etiam est nunc venenatis in tristique eu imperdiet ac nisl Cum sociis natoque penatibus et magnis dis parturient montes nascetur ridiculus mus In iaculis facilisis massa Etiam eu urna Sed porta Suspendisse quam leo molestie sed luctus quis feugiat</p>
<div class="video abs">
  <div class="video-still abs" role="img" aria-label="Pianist in a dark suit and tie seated at the piano"></div>
  <svg class="video-play abs" width="30" height="30"><circle cx="15" cy="15" r="13.5" fill="none" stroke="#fff" stroke-width="2"/><polygon points="12,9.5 21,15 12,20.5" fill="#fff"/></svg>
</div>

<section class="testimonials abs">
  <svg class="testimonials-bg abs" width="740" height="222" role="img" aria-label="Antique grand piano in an ornate golden room, tinted orange"><defs><linearGradient id="warm" x1="0" y1="0" x2="1" y2="0"><stop offset="0" stop-color="#ee8f33"/><stop offset=".6" stop-color="#f0a25a"/><stop offset="1" stop-color="#ee8f33"/></linearGradient></defs><polygon points="0,0 740,7 740,222 0,222" fill="url(#warm)"/></svg>
  <h2 class="testimonials-title abs">What My Students Say</h2>
  <figure class="quote q1 abs"><div class="quote-avatar abs" role="img" aria-label="Student portrait"></div><p>Aliquam nec erat at purus cursus interdum Vestibulum ligula augue bibendum accum-san vestibulum ut commodo a mi Morbi ornare gravida elit</p><cite>By Author Name</cite></figure>
  <figure class="quote q2 abs"><div class="quote-avatar abs" role="img" aria-label="Student portrait"></div><p>Aliquam nec erat at purus cursus interdum Vestibulum ligula augue bibendum accum-san vestibulum ut commodo a mi Morbi ornare gravida elit</p><cite>By Author Name</cite></figure>
  <figure class="quote q3 abs"><div class="quote-avatar abs" role="img" aria-label="Student portrait"></div><p>Aliquam nec erat at purus cursus interdum Vestibulum ligula augue bibendum accum-san vestibulum ut commodo a mi Morbi ornare gravida elit</p><cite>By Author Name</cite></figure>
</section>

<footer class="site-footer abs">
  <nav class="footer-nav abs">HOME<span>/</span>ABOUT ME<span>/</span>SERVICES<span>/</span>BLOG<span>/</span>TESTIMONIAL<span>/</span>CONTACT</nav>
  <p class="copyright abs">© 2014 Company Name &nbsp;All right reserved &nbsp;Term of Use</p>
  <div class="social abs" aria-label="Social links"><i></i><i></i><i></i></div>
</footer>

</body>
</html>
```